Woman owned consulting company needs an elegant and modern business card design

I need a business card design for my new consulting company, Mara Quill Consulting. I am looking for something that is simple and elegant, but also creative and original. You can use either version of the logo that are attached. I have also included the information that needs to be featured on the business card.

Requirements
Must have
• The logo and the font type and a standard business card size. Use shades of gray/silver and or rose gold that are in the logo.
• I didn't realize that my actual logo wasn't attached. Please incorporate in the designs.
Should not have
• Colors that are different from my logo

```html
<!DOCTYPE html>
<html lang="en">
<head>
<meta charset="utf-8">
<title>Mara Quill Consulting — Business Card</title>
<link href="https://fonts.googleapis.com/css2?family=Cinzel:wght@400;600&family=Cormorant+Garamond:wght@500;600&display=swap" rel="stylesheet">
<style>
  :root {
    --backdrop: #a3a3a3;
    --card-mist: #ebe3dd;
    --card-chocolate: #3b2b27;
    --ink-brown: #3f302c;
    --foil-gold: #b9a57a;
    --card-shadow: rgba(0, 0, 0, 0.28);
  }
  html, body {
    margin: 0;
    padding: 0;
    width: 1200px;
    height: 1016px;
    overflow: hidden;
    background: var(--backdrop);
  }
  .canvas {
    position: relative;
    width: 1200px;
    height: 1016px;
  }
  .card {
    position: absolute;
    left: 332px;
    width: 549px;
    height: 314px;
    box-shadow: 4px 10px 18px var(--card-shadow);
    display: flex;
    flex-direction: column;
    align-items: center;
    box-sizing: border-box;
  }
  .card--front {
    top: 131px;
    background: var(--card-mist);
    color: var(--ink-brown);
  }
  .card--back {
    top: 513px;
    background: var(--card-chocolate);
    justify-content: center;
  }
  .holder-name {
    margin: 44px 0 0;
    font-family: "Cinzel", serif;
    font-weight: 600;
    font-size: 33px;
    line-height: 1;
    letter-spacing: 0.5px;
  }
  .holder-role {
    margin: 6px 0 0;
    font-family: "Cinzel", serif;
    font-size: 13px;
    letter-spacing: 15px;
    padding-left: 15px;
  }
  .brand-name {
    margin: 0;
    font-family: "Cinzel", serif;
    font-weight: 400;
    color: var(--foil-gold);
    text-align: center;
    line-height: 1.2;
  }
  .card--front .brand-name {
    margin-top: 56px;
    font-size: 20px;
    letter-spacing: 2px;
  }
  .card--back .brand-name {
    font-size: 34px;
    letter-spacing: 3px;
  }
  .contact-line {
    margin: auto 0 40px;
    font-family: "Cormorant Garamond", serif;
    font-weight: 600;
    font-size: 15px;
    letter-spacing: 0.3px;
  }
</style>
</head>
<body>
  <main class="canvas">
    <section class="card card--front" aria-label="Business card front">
      <h1 class="holder-name">MARA QUILL</h1>
      <p class="holder-role">OWNER</p>
      <p class="brand-name">Mara Quill Consulting</p>
      <p class="contact-line">555-014-2290 / WWW.MARAQUILLCONSULTING.COM</p>
    </section>
    <section class="card card--back" aria-label="Business card back">
      <p class="brand-name">Mara Quill Consulting</p>
    </section>
  </main>
</body>
</html>
```